Flyer Needed for Westland Advocacy Summit 2017

We need a flyer designed for a save the date for Verdant Goods Forum in California on August 23, 2017. The lobby day is taking place in Sacramento so please design the flyer using these details.

Requirements
Must have
• - Date must be clear
Nice to have
• - Must have "save the date"
• - Something that catches your eye

```html
<!DOCTYPE html>
<html lang="en">
<head>
<meta charset="utf-8">
<title>Save the Date – Verdant Goods Forum</title>
<link rel="stylesheet" href="https://fonts.googleapis.com/css2?family=Montserrat:wght@400;500&family=Oswald:wght@700&display=swap">
<style>
  :root {
    --sky-light: #9cbd74;
    --sky-mid: #6f9450;
    --shadow-deep: #1a2414;
    --ink-green: #34492a;
    --ring-line: #3a5230;
    --badge-white: #ffffff;
    --text-light: #ffffff;
  }
  * { margin: 0; padding: 0; box-sizing: border-box; }
  html, body { width: 872px; height: 1200px; overflow: hidden; background: #f2f2f2; }
  .poster {
    position: relative;
    width: 872px;
    height: 1200px;
    overflow: hidden;
    font-family: "Montserrat", Arial, sans-serif;
  }
  .city-photo {
    position: absolute;
    inset: 0;
    background:
      radial-gradient(ellipse at 75% 45%, rgba(60, 80, 45, 0.55), transparent 60%),
      linear-gradient(180deg, var(--sky-light) 0%, #87ab63 30%, var(--sky-mid) 55%, #3d5530 78%, var(--shadow-deep) 100%);
  }
  .date-badge {
    position: absolute;
    left: 0;
    top: 0;
    width: 872px;
    height: 1200px;
  }
  .badge-text {
    position: absolute;
    left: 0;
    width: 872px;
    text-align: center;
    color: var(--ink-green);
  }
  .save-the-date { top: 462px; font-size: 34px; font-weight: 500; letter-spacing: 1px; }
  .for-line { top: 506px; font-size: 28px; font-weight: 500; }
  .event-name {
    top: 540px;
    font-family: "Oswald", "Arial Narrow", sans-serif;
    font-weight: 700;
    font-size: 74px;
    line-height: 76px;
    text-transform: uppercase;
  }
  .event-date { top: 710px; font-size: 46px; font-weight: 500; letter-spacing: 1px; color: #3a5a2a; }
  .venue {
    position: absolute; left: 0; width: 872px; top: 962px;
    text-align: center; color: var(--text-light);
    font-size: 35px; font-weight: 500;
  }
  .details {
    position: absolute; left: 0; width: 872px; top: 1106px;
    text-align: center; color: var(--text-light);
    font-size: 19px; font-weight: 400; letter-spacing: 0.3px;
  }
</style>
</head>
<body>
<main class="poster">
  <div class="city-photo" role="img" aria-label="Night photograph of a suspension bridge and city skyline, tinted green"></div>

  <svg class="date-badge" viewBox="0 0 872 1200" aria-hidden="true">
    <circle cx="436" cy="604" r="322" fill="rgba(255,255,255,0.18)"/>
    <circle cx="436" cy="604" r="292" fill="rgba(255,255,255,0.22)"/>
    <circle cx="436" cy="604" r="260" fill="var(--badge-white)" stroke="var(--ring-line)" stroke-width="4"/>
  </svg>

  <p class="badge-text save-the-date">SAVE THE DATE</p>
  <p class="badge-text for-line">for</p>
  <h1 class="badge-text event-name">Verdant<br>Goods Forum</h1>
  <p class="badge-text event-date">23.08.2017</p>

  <p class="venue">Sacramento, California</p>
  <p class="details">For more details visit us @ www.verdantgoodsforum.org</p>
</main>
</body>
</html>
```